Discreet simple classy for adult entertainment

I would like a matte black business card with gold writing for my business. Keeping it simple. Having my following:

Lana frost
Events. Entertainment. Promotions
0491726580

or alternatively could have what i had on my previous card below but i think i prefer the above as again - discretion.

Maybe a nice gold line thru the card or some other very simple design . Or not open to ideas/ can be doublesided if any good ideas with that.

included pics of my old bus card. not sure weather i want a photo on it or not. if i do it wont be the same pic. i kinda wanted a card that was discreet so if it was in someones wallet they wouldn't neccessarily realise it was from a stripper.

Target Market(s)

men

Industry/Entity Type

Business

Contact Information for Business Card

Lana frost
0491726580

Requirements
Nice to have
• i don't know i am really open to anything. im giving my cards to guys so something they can have in their wallet that is discreet preferably.

```html
<!DOCTYPE html>
<html lang="en">
<head>
<meta charset="utf-8">
<title>Lana frost — Business Card</title>
<link rel="stylesheet" href="https://fonts.googleapis.com/css2?family=Cinzel:wght@400;500&display=swap">
<style>
  :root {
    --card-black: #000000;
    --text-gold: #f4df0c;
    --figure-lime: #dcf01a;
    --band-yellow: #fde31a;
  }
  html, body {
    margin: 0;
    padding: 0;
    width: 1200px;
    height: 686px;
    overflow: hidden;
    background: var(--card-black);
  }
  .card {
    position: relative;
    width: 1200px;
    height: 686px;
    background: var(--card-black);
    font-family: "Cinzel", "Trajan Pro", serif;
    color: var(--text-gold);
    overflow: hidden;
  }
  .dancer-figure {
    position: absolute;
    left: 34px;
    top: 34px;
    width: 172px;
    height: 396px;
    background: linear-gradient(180deg, var(--figure-lime), #c9de12);
    border-radius: 40px 40px 20px 20px;
  }
  .name {
    position: absolute;
    left: 266px;
    top: 182px;
    margin: 0;
    font-size: 112px;
    font-weight: 500;
    letter-spacing: 4px;
    line-height: 1;
    white-space: nowrap;
  }
  .phone {
    position: absolute;
    left: 398px;
    top: 358px;
    margin: 0;
    font-size: 50px;
    font-weight: 400;
    letter-spacing: 6px;
    line-height: 1;
  }
  .services {
    position: absolute;
    left: 129px;
    top: 462px;
    margin: 0;
    font-size: 47px;
    font-weight: 400;
    letter-spacing: 3px;
    line-height: 1;
    white-space: nowrap;
  }
  .bottom-band {
    position: absolute;
    left: 0;
    bottom: 0;
    width: 1200px;
    height: 70px;
  }
</style>
</head>
<body>
  <div class="card">
    <div class="dancer-figure" role="img" aria-label="Lime silhouette of a dancer posed on a vertical pole"></div>

    <h1 class="name">Lana frost</h1>
    <p class="phone">0491726580</p>
    <p class="services">events / &nbsp;Entertainment / promotions</p>

    <svg class="bottom-band" viewBox="0 0 1200 70" preserveAspectRatio="none" aria-hidden="true">
      <path d="M0 8 Q600 32 1200 34 L1200 70 L0 70 Z" fill="var(--band-yellow)"/>
    </svg>
  </div>
</body>
</html>
```